Webdesign for development of custom specific electronics
Zielgruppe
We are specialised in development of custom specific electronics.
We also produce and test the pcb assemblies for our customers .
We sell some of our own products as well.
Aufgabenstellung
We provide an detailed briefing in a separate file.

```html
<!DOCTYPE html>
<html lang="de">
<head>
<meta charset="utf-8">
<title>Trusk Halvorsen – Elektronikentwicklung</title>
<link rel="stylesheet" href="https://fonts.googleapis.com/css2?family=Source+Sans+3:wght@300;400;600&family=Comfortaa:wght@400;600&display=swap">
<style>
  :root{
    --ink:#1f2326;
    --grey:#6e7377;
    --nav:#2a2d30;
    --panel:rgba(228,232,234,.9);
    --deep:#062a3a;
    --teal:#1fb7b4;
    --cube-green:#4fbf5a;
    --cube-blue:#3446b8;
    --cube-pink:#c04bd0;
    --logo-blue:#1f72c9;
  }
  *{margin:0;padding:0;box-sizing:border-box}
  html,body{width:877px;height:1200px;overflow:hidden;background:#fff}
  body{position:relative;font-family:"Source Sans 3",sans-serif;color:var(--ink)}
  .abs{position:absolute}

  .header{left:0;top:0;width:877px;height:313px;background:linear-gradient(#fff 70%,#eceef0)}
  .hero-blocks{left:64px;top:27px;width:297px;height:262px;border-radius:4px;
    background:linear-gradient(135deg,#1f8d3a,#9fe7a8 40%,#a3202a 60%,#6ed278)}
  .nav{left:322px;top:12px;display:flex;gap:8px;font-size:10.6px;color:var(--nav);letter-spacing:.1px}
  .tagline{left:377px;top:74px;font-family:"Comfortaa",sans-serif;color:var(--grey);white-space:nowrap}
  .tagline .small{font-size:15px}
  .tagline .mid{font-size:28px}
  .tagline .big{font-size:50px;font-weight:600}
  .brand{left:520px;top:208px;display:flex;align-items:center;gap:8px}
  .brand .mark{width:18px;height:18px;background:var(--logo-blue)}
  .brand .name{font-size:22px;font-weight:600;color:#3c4044}
  .brand-sub{left:560px;top:248px;width:228px;text-align:right;font-size:9.5px;line-height:13px;color:#55595c}

  .stage{left:22px;top:313px;width:835px;height:887px;
    background:radial-gradient(ellipse at 85% 50%,var(--teal),#0d6672 45%,var(--deep) 80%)}
  .hand{left:486px;top:313px;width:371px;height:112px;
    background:linear-gradient(90deg,rgba(220,170,140,0),#d9a888 40%,#c58e70 80%,#3c4a5a)}

  .panel{background:var(--panel)}
  .panel h2{font-weight:400;font-size:16.5px;line-height:19px;margin-bottom:6px}
  .panel p{font-size:11.8px;font-weight:400}

  .cube{border:1px solid #2b3a2e}
  .cube.green{background:linear-gradient(135deg,#2f8a3a,var(--cube-green) 50%,#b8f0b8)}
  .cube.blue{background:linear-gradient(135deg,#2030a0,var(--cube-blue) 50%,#c8d2f2)}
  .cube.pink{background:linear-gradient(135deg,#7a2a90,var(--cube-pink) 50%,#f0c8f2)}
</style>
</head>
<body>
  <header class="abs header">
    <div class="abs hero-blocks" role="img" aria-label="Gestapelte Würfel mit Leiterplattenmotiv"></div>
    <nav class="abs nav">
      <span>ENTWICKLUNG</span><span>FERTIGUNG</span><span>SERVICE</span><span>REFERENZEN</span><span>ERFOLGSSTORIES</span><span>ÜBER UNS</span><span>KONTAKT</span><span>IMPRESSUM</span>
    </nav>
    <div class="abs tagline"><span class="small">…ein Baustein zu </span><span class="mid">Ihrem </span><span class="big">Erfolg</span></div>
    <div class="abs brand"><span class="mark"></span><span class="name">Trusk Halvorsen</span></div>
    <div class="abs brand-sub">Elektronikentwicklung und<br>Fertigung von Schaltungen &amp; Baugruppen</div>
  </header>

  <main>
    <div class="abs stage" role="img" aria-label="Leuchtende Leiterbahnen in Türkis auf dunklem Grund"></div>
    <div class="abs hand" role="img" aria-label="Hand, die einen Baustein einsetzt"></div>

    <section class="abs panel" style="left:36px;top:321px;width:551px;height:144px;padding:12px 22px">
      <h2>Entwicklung</h2>
      <p style="width:330px;line-height:21px">Die moderne Elektronikentwicklung lässt sich in zwei Bereiche unterteilen, welche sehr eng miteinander verzahnt sind: Auf der einen Seite die Hardwareentwicklung, auf der anderen die Softwareentwicklung.</p>
    </section>
    <div class="abs cube green" style="left:459px;top:372px;width:90px;height:77px" role="img" aria-label="Würfel mit grünem Leiterplattenmotiv"></div>

    <section class="abs panel" style="left:288px;top:486px;width:551px;height:223px;padding:10px 20px 0 188px">
      <h2>Hardware-Entwicklung</h2>
      <p style="line-height:24.4px">Alles beginnt mit einer Idee. Mit dieser wenden Sie sich an uns.Gemeinsam mit Ihnen erstellen wir ein Lastenheft. Dabei nehmen wir Sie „an die Hand“ und klären mit Ihnen alle notwendigen Punkte ab. Besonders wichtig sind in diesem ersten Schritt fundamentale Anforderungen wie beispielsweise: Umwelteinflüsse, Batterielaufzeiten, Bedienkonzepte und vieles mehr.</p>
    </section>
    <div class="abs cube blue" style="left:218px;top:520px;width:162px;height:141px" role="img" aria-label="Würfel mit blauem Leiterplattenmotiv"></div>

    <section class="abs panel" style="left:36px;top:723px;width:551px;height:226px;padding:12px 17px">
      <h2>Software Entwicklung</h2>
      <p style="width:330px;line-height:24.4px">n der heutigen Zeit füllt die Software jedes Gerät mit Leben. Eine gute Software ist intuitiv, einfach und stabil. Und aktuell. Dafür stellen wir moderne Updatemöglichekeiten zur Verfügung, wie Firmewareupdate „Over The Air“ (OTA), über das Internet oder über wechselbare Speichermedien. Sie können besonders schnell auf Kundenwünsche reagieren oder Probleme schon im Vorfeld erkennen.</p>
    </section>
    <div class="abs cube green" style="left:507px;top:767px;width:162px;height:144px" role="img" aria-label="Würfel mit grünem Leiterplattenmotiv"></div>

    <section class="abs panel" style="left:292px;top:966px;width:550px;height:221px;padding:14px 20px 0 158px">
      <h2 style="font-size:17px;line-height:21px">Entwicklung von Applikationssoftware (PC / (embedded) Linux und Server):</h2>
      <p style="line-height:24.4px">Neben der Firmwareentwicklung bieten wir zudem die Erstellung von Desktop-, Web-Anwedungen (GUIs) sowie die dazugehörigen Server-Backend Lösungen an.</p>
    </section>
    <div class="abs cube pink" style="left:194px;top:1006px;width:167px;height:151px" role="img" aria-label="Würfel mit violettem Leiterplattenmotiv"></div>
  </main>
</body>
</html>
```